its a new company based in Christchurch new Zealand building computers ,repairs, upgrades and anything computers for the general public,i like bright happy colours like yellows, greens reds anything that stands out and it needs to communicant trust and security towards my new company,i have no logo yet,

Target Market(s)

target market of all ages

Industry/Entity Type

Building

Contact Information for Business Card

Pixel Harbour Limited,ph-0274829315,email-brightnode47@mailvista.example,14c tamworth cl,kelvale

```html
<!DOCTYPE html>
<html lang="en">
<head>
<meta charset="UTF-8">
<title>Pixel Harbour Limited – Business Card</title>
<link href="https://fonts.googleapis.com/css2?family=Exo+2:wght@400;600&display=swap" rel="stylesheet">
<style>
  :root {
    --card-bg: #e8e8e8;
    --brand-blue: #2a6db8;
    --brand-orange: #f7941d;
    --rule-blue: #5a7fb5;
  }
  html, body {
    margin: 0;
    padding: 0;
    width: 1200px;
    height: 741px;
    overflow: hidden;
    background: var(--card-bg);
  }
  .card {
    position: relative;
    width: 1200px;
    height: 741px;
    background: var(--card-bg);
    font-family: "Exo 2", sans-serif;
    text-align: center;
  }
  .card > * {
    position: absolute;
    left: 0;
    width: 100%;
    margin: 0;
    line-height: 1;
  }
  .company-name {
    top: 151px;
    font-size: 50px;
    font-weight: 600;
    color: var(--brand-blue);
  }
  .contact-label {
    font-size: 19px;
    font-weight: 400;
    color: var(--brand-orange);
    letter-spacing: 0.5px;
  }
  .label-phone { top: 242px; }
  .label-email { top: 321px; }
  .phone-number {
    top: 259px;
    font-size: 44px;
    font-weight: 400;
    color: var(--brand-blue);
  }
  .email-address {
    top: 341px;
    font-size: 33px;
    font-weight: 400;
    color: var(--brand-blue);
  }
  .divider {
    top: 399px;
    left: 357px;
    width: 484px;
    height: 1px;
    background: var(--rule-blue);
  }
  .street-address {
    top: 426px;
    font-size: 31px;
    font-weight: 400;
    color: var(--brand-orange);
  }
  .brand-wordmark {
    top: 567px;
    font-size: 42px;
    font-weight: 600;
    color: var(--brand-blue);
    letter-spacing: 1px;
  }
</style>
</head>
<body>
  <main class="card">
    <h1 class="company-name">Pixel Harbour Limited</h1>

    <p class="contact-label label-phone">PHONE</p>
    <p class="phone-number">0274829315</p>

    <p class="contact-label label-email">EMAIL</p>
    <p class="email-address">brightnode47@mailvista.example</p>

    <div class="divider"></div>

    <p class="street-address">14C Tamworth Cl, Kelvale</p>

    <p class="brand-wordmark">PIXEL HARBOUR</p>
  </main>
</body>
</html>
```